Website for vegan focused blog

A website is needed so that I can launch my new blog in Dubai. It will be mainly vegan focused but also lifestyle based. Wordpress based- i started to build a site on Wordpress but design is not my forte ;)
Main content on the site will be; my recipes, reviews of products/restaurants, lifestyle posts and travel.
For this I ask for a homepage design, a recipe design page that includes a recipe card and a generic page for posts that can show pictures and videos. Also a contact me page.
Main headers should be: Home, Recipes and happy for suggestions.
Must look clean and neat but appealing, happy for minimalist look. I like pink and grey colours. Must be Wordpress compatible.
Have attached a couple of example posts for reference
Must have social links etc.
name of blog is: Maddie on the dunes
Other blogs I like are: https://sparsekitchen.example/ https://thyleafshines.example/ https://thyleafshines.example/ https://www.ohladycakes.com/https://lentilsforsupper.example/ https://jorunbeck.example/

Target Market(s)

Residents in the UAE. General individuals interested in vegan meals, plant based nutrition, travel and reviews.

Number of Pages Required

4 page

Colors
eea4c8
eda3c7
f9d9e8
dbdbdb
aaaaaa
d5d5d5

Requirements
Must have
• Recipe page- must include recipe card plug in option
• Social media integration
• Email sign ups

```html
<!DOCTYPE html>
<html lang="en">
<head>
<meta charset="utf-8">
<title>Maddie on the dunes</title>
<link href="https://fonts.googleapis.com/css2?family=Lato:wght@300;400;700&family=Lora:ital,wght@0,400;1,400&display=swap" rel="stylesheet">
<style>
  :root {
    --pink: #d9a4c7;
    --pink-deep: #c98db5;
    --blush: #f2d9e7;
    --ink: #1d1d1d;
    --text: #3a3a3a;
    --muted: #8a8a8a;
    --rule: #ebebeb;
    --field: #dbdbdb;
    --white: #ffffff;
  }
  * { box-sizing: border-box; margin: 0; padding: 0; }
  html, body { width: 703px; height: 1200px; overflow: hidden; background: var(--white); }
  body { position: relative; font-family: "Lora", Georgia, serif; color: var(--text); }
  .abs { position: absolute; }

  .top-nav { left: 0; top: 0; width: 703px; height: 18px; background: var(--pink); display: flex; justify-content: center; align-items: center; gap: 30px; }
  .top-nav a { font-family: "Lato", sans-serif; font-size: 4.6px; letter-spacing: 0.9px; color: var(--ink); text-decoration: none; text-transform: uppercase; }

  .masthead { left: 0; top: 18px; width: 703px; height: 74px; background: var(--blush); display: flex; justify-content: center; align-items: center; }
  .site-title { font-family: "Lato", sans-serif; font-weight: 300; font-size: 18px; letter-spacing: 2.4px; color: var(--ink); text-transform: uppercase; }

  .photo { background: linear-gradient(135deg, #e7ece4 0%, #b9c3a2 30%, #5a2c2a 48%, #7b3c3a 62%, #b7bf9b 85%, #eef0ea 100%); }
  .photo-person { background: linear-gradient(180deg, #eee9ea 0%, #e9d7d2 55%, #d6b49a 72%, #a98c78 100%); }
  .avatar { border-radius: 50%; background: #c9c9c9; }

  .heading { font-family: "Lato", sans-serif; font-weight: 700; text-transform: uppercase; color: var(--ink); letter-spacing: 1.2px; }
  .card-title { font-size: 7px; text-align: center; }
  .excerpt { font-size: 5.1px; line-height: 8px; color: var(--text); }
  .btn { background: var(--pink); border: 1px solid var(--pink-deep); font-family: "Lato", sans-serif; font-size: 4.8px; letter-spacing: 1px; text-transform: uppercase; color: var(--ink); display: flex; align-items: center; justify-content: center; }
  .rule { height: 1px; background: var(--rule); }

  .label { font-family: "Lato", sans-serif; font-weight: 700; font-size: 3.8px; letter-spacing: 0.8px; text-transform: uppercase; color: var(--ink); }
  .caption { font-family: "Lato", sans-serif; font-size: 3.6px; letter-spacing: 0.6px; text-transform: uppercase; color: var(--muted); }
  .field { border: 1px solid var(--rule); font-style: italic; font-size: 4.6px; color: var(--ink); display: flex; align-items: center; padding-left: 8px; }
  .field.dark { border-color: var(--ink); }
  .widget-link { font-style: italic; font-size: 4.6px; color: var(--ink); }
  .date { font-family: "Lato", sans-serif; font-size: 3.8px; letter-spacing: 0.6px; color: var(--muted); text-align: center; text-transform: uppercase; }
</style>
</head>
<body>

<nav class="abs top-nav">
  <a href="#">Recipes</a><a href="#">Travel</a><a href="#">Lifestyle</a><a href="#">Reviews</a><a href="#">Contact Page</a>
</nav>

<header class="abs masthead"><h1 class="site-title">Maddie on the dunes</h1></header>

<!-- Featured recipes -->
<section class="featured">
  <div class="abs photo" style="left:133px;top:107px;width:138px;height:91px" role="img" aria-label="Grilled portobello mushroom steak on herb mash"></div>
  <h2 class="abs heading card-title" style="left:133px;top:206px;width:138px">Mushroom Steak</h2>
  <p class="abs excerpt" style="left:133px;top:220px;width:138px">Mushroom Stek Steak and vegan don't go in the same sentence BUT trust me on this..a decent sized Portobello shroom cooked just right with a blend ...</p>
  <a class="abs btn" style="left:168px;top:256px;width:67px;height:20px">Read More</a>

  <div class="abs photo" style="left:282px;top:107px;width:139px;height:91px" role="img" aria-label="Grilled portobello mushroom steak on herb mash"></div>
  <h2 class="abs heading card-title" style="left:282px;top:206px;width:139px">Mushroom Steak</h2>
  <p class="abs excerpt" style="left:282px;top:220px;width:139px">Mushroom Stek Steak and vegan don't go in the same sentence BUT trust me on this..a decent sized Portobello shroom cooked just right with a blend ...</p>
  <a class="abs btn" style="left:318px;top:256px;width:67px;height:20px">Read More</a>

  <div class="abs photo" style="left:432px;top:107px;width:138px;height:91px" role="img" aria-label="Grilled portobello mushroom steak on herb mash"></div>
  <h2 class="abs heading card-title" style="left:432px;top:206px;width:138px">Mushroom Steak</h2>
  <p class="abs excerpt" style="left:432px;top:220px;width:138px">Mushroom Stek Steak and vegan don't go in the same sentence BUT trust me on this..a decent sized Portobello shroom cooked just right with a blend ...</p>
  <a class="abs btn" style="left:468px;top:256px;width:67px;height:20px">Read More</a>
</section>

<div class="abs rule" style="left:133px;top:304px;width:437px"></div>

<!-- Newsletter row -->
<section class="newsletter">
  <h3 class="abs heading" style="left:133px;top:325px;font-size:5.6px;font-weight:400">Never miss a recipe</h3>
  <p class="abs" style="left:218px;top:325px;font-size:4.8px;font-style:italic;color:var(--ink)">Sign up to get new recipes via email.</p>
  <div class="abs field dark" style="left:352px;top:319px;width:135px;height:16px">e-mail address</div>
  <a class="abs btn" style="left:487px;top:319px;width:83px;height:16px">Subscribe</a>
</section>

<!-- About -->
<section class="about">
  <div class="abs photo-person" style="left:133px;top:359px;width:122px;height:122px" role="img" aria-label="Woman walking on a beach at sunset"></div>
  <h2 class="abs heading" style="left:270px;top:359px;width:300px;font-size:7px;text-align:center">About Me</h2>
  <p class="abs excerpt" style="left:270px;top:372px;width:300px">On Maddie on the dunes, I share some delicious recipes either my own or from other fabulous sites that I have come across, my meal plans, reviews of products and restaurants that I visit and more. And yes, I live on a plant based diet. Shock.. horror..brakes on...leaves site... ! Just hear me out a minute... I am not going to lecture you about becoming vegan or being plant powered or eating cruelty free. If you are looking for Plant Plate Monday inspiration, perhaps you want to try a plant based diet for a week or just looking to save some cash with some veggie recipes, I hope this is where I can help. And this is what I want to achieve; as small changes can make a big difference right? And for my fellow plant food lovers...hopefully you will find some inspiration! So a little bit about me... ...</p>
  <a class="abs btn" style="left:387px;top:442px;width:67px;height:20px">Read More</a>
</section>

<div class="abs rule" style="left:133px;top:492px;width:437px"></div>

<!-- Post list -->
<main class="posts">
  <article>
    <div class="abs photo" style="left:133px;top:516px;width:104px;height:77px" role="img" aria-label="Grilled portobello mushroom steak on herb mash"></div>
    <p class="abs date" style="left:252px;top:517px;width:142px">October 14, 2018</p>
    <h2 class="abs heading" style="left:252px;top:526px;width:142px;font-size:7px;text-align:center">Mushroom Steak</h2>
    <p class="abs excerpt" style="left:252px;top:540px;width:140px">Print Mushroom Stek Steak and vegan don't go in the same sentence BUT trust me on this..a decent sized Portobello shroom cooked just right with a blend of delicious marinade, it has the meatiest texture and its delicious as well oh and did we mention it is completely cruelty free!?To get the right texture you...</p>
    <a class="abs btn" style="left:230px;top:601px;width:66px;height:20px">Read More</a>
  </article>
  <div class="abs rule" style="left:133px;top:640px;width:261px"></div>

  <article>
    <div class="abs photo" style="left:133px;top:657px;width:104px;height:77px" role="img" aria-label="Grilled portobello mushroom steak on herb mash"></div>
    <p class="abs date" style="left:252px;top:658px;width:142px">October 14, 2018</p>
    <h2 class="abs heading" style="left:252px;top:667px;width:142px;font-size:7px;text-align:center">Mushroom Steak</h2>
    <p class="abs excerpt" style="left:252px;top:681px;width:140px">Print Mushroom Stek Steak and vegan don't go in the same sentence BUT trust me on this..a decent sized Portobello shroom cooked just right with a blend of delicious marinade, it has the meatiest texture and its delicious as well oh and did we mention it is completely cruelty free!?To get the right texture you...</p>
    <a class="abs btn" style="left:230px;top:741px;width:66px;height:20px">Read More</a>
  </article>
  <div class="abs rule" style="left:133px;top:781px;width:261px"></div>

  <article>
    <div class="abs photo" style="left:133px;top:797px;width:104px;height:77px" role="img" aria-label="Grilled portobello mushroom steak on herb mash"></div>
    <p class="abs date" style="left:252px;top:798px;width:142px">October 14, 2018</p>
    <h2 class="abs heading" style="left:252px;top:807px;width:142px;font-size:7px;text-align:center">Mushroom Steak</h2>
    <p class="abs excerpt" style="left:252px;top:821px;width:140px">Print Mushroom Stek Steak and vegan don't go in the same sentence BUT trust me on this..a decent sized Portobello shroom cooked just right with a blend of delicious marinade, it has the meatiest texture and its delicious as well oh and did we mention it is completely cruelty free!?To get the right texture you...</p>
    <a class="abs btn" style="left:230px;top:882px;width:66px;height:20px">Read More</a>
  </article>
  <div class="abs rule" style="left:133px;top:922px;width:261px"></div>
</main>

<!-- Sidebar -->
<aside class="sidebar">
  <div class="abs field" style="left:455px;top:517px;width:71px;height:15px;font-size:4.2px">Search this website ...</div>
  <div class="abs field" style="left:526px;top:517px;width:44px;height:15px;font-style:normal;font-family:'Lato',sans-serif;font-size:3.8px;letter-spacing:0.8px;color:#c8c8c8;justify-content:center;padding:0">SEARCH</div>

  <h4 class="abs label" style="left:455px;top:557px">Recent Comments</h4>
  <div class="abs rule" style="left:455px;top:576px;width:115px"></div>

  <h4 class="abs label" style="left:455px;top:591px">Archives</h4>
  <p class="abs widget-link" style="left:455px;top:601px">• October 2018</p>
  <div class="abs rule" style="left:455px;top:623px;width:115px"></div>

  <h4 class="abs label" style="left:455px;top:633px">Categories</h4>
  <p class="abs widget-link" style="left:455px;top:643px">Lifestyle</p>
  <p class="abs widget-link" style="left:455px;top:651px">Recipe</p>
  <div class="abs rule" style="left:455px;top:674px;width:115px"></div>

  <h4 class="abs label" style="left:455px;top:684px">Don't miss these!</h4>
  <div class="abs photo" style="left:455px;top:693px;width:56px;height:55px" role="img" aria-label="Mushroom steak thumbnail"></div>
  <div class="abs photo" style="left:514px;top:693px;width:56px;height:55px" role="img" aria-label="Mushroom steak thumbnail"></div>
  <p class="abs caption" style="left:455px;top:758px">Mushroom Steak</p>
  <p class="abs caption" style="left:514px;top:758px">Mushroom Steak</p>
  <div class="abs photo" style="left:455px;top:772px;width:56px;height:55px" role="img" aria-label="Mushroom steak thumbnail"></div>
  <p class="abs caption" style="left:455px;top:836px">Mushroom Steak</p>
  <div class="abs rule" style="left:455px;top:866px;width:115px"></div>

  <h4 class="abs label" style="left:455px;top:876px">Most Popular Recipes</h4>
  <div class="abs photo" style="left:455px;top:885px;width:46px;height:30px" role="img" aria-label="Mushroom steak thumbnail"></div>
  <p class="abs caption" style="left:505px;top:885px">Mushroom Steak</p>
  <div class="abs photo" style="left:455px;top:921px;width:46px;height:30px" role="img" aria-label="Mushroom steak thumbnail"></div>
  <p class="abs caption" style="left:505px;top:922px">Mushroom Steak</p>
  <div class="abs rule" style="left:455px;top:974px;width:115px"></div>

  <h4 class="abs label" style="left:455px;top:989px">Stay Updated</h4>
  <div class="abs field" style="left:455px;top:1001px;width:115px;height:17px">First Name</div>
  <div class="abs field" style="left:455px;top:1022px;width:115px;height:17px">Last Name</div>
  <div class="abs field" style="left:455px;top:1042px;width:115px;height:17px">E-Mail Address</div>
  <a class="abs btn" style="left:455px;top:1063px;width:115px;height:16px">Subscribe</a>
  <div class="abs rule" style="left:455px;top:1098px;width:115px"></div>
</aside>

<!-- Footer widgets -->
<footer class="footer">
  <h4 class="abs label" style="left:133px;top:1131px;font-weight:400">About your designer</h4>
  <div class="abs avatar" style="left:133px;top:1142px;width:31px;height:31px" role="img" aria-label="Default profile placeholder"></div>
  <p class="abs excerpt" style="left:173px;top:1141px;width:98px">Brand + web designer creating clear, compelling sites for food &amp; lifestyle bloggers taking the leap from blog-to-business!</p>

  <h4 class="abs label" style="left:282px;top:1131px;font-weight:400">My Favorites</h4>
  <div class="abs photo" style="left:284px;top:1143px;width:38px;height:37px" role="img" aria-label="Mushroom steak thumbnail"></div>
  <div class="abs photo" style="left:329px;top:1143px;width:38px;height:37px" role="img" aria-label="Mushroom steak thumbnail"></div>
  <div class="abs photo" style="left:374px;top:1143px;width:38px;height:37px" role="img" aria-label="Mushroom steak thumbnail"></div>

  <h4 class="abs label" style="left:432px;top:1131px;font-weight:400">Stay Connected</h4>
  <svg class="abs" style="left:432px;top:1139px" width="80" height="14" viewBox="0 0 80 14" aria-label="Social links">
    <g fill="none" stroke="#c9c9c9" stroke-width="0.8">
      <circle cx="7" cy="7" r="5.5"/><circle cx="23" cy="7" r="5.5"/><circle cx="39" cy="7" r="5.5"/><circle cx="55" cy="7" r="5.5"/><circle cx="71" cy="7" r="5.5"/>
    </g>
  </svg>
  <div class="abs field dark" style="left:432px;top:1160px;width:86px;height:16px">E-Mail Address</div>
  <a class="abs btn" style="left:518px;top:1160px;width:52px;height:16px">Subscribe</a>
</footer>

</body>
</html>
```